Butcher shop

We have 2 butcher shops:

Shop 9, Ridgeway Court, Bellmoor NSW 2341
Ph 02 6512 3840

47 Marlow St, Corrindale NSW 2344
Ph 02 6518 2274

ABN 48 907 215 816

I would like this info on reverse of card and my personal info on front of card. I have a logo I would like to use also. Require a very smooth thick matte card, with colour both sides.

Front of card should say:

Linda Farrugia
Accounts

Ph 0437 620 915
E lindafarrugia@quollmail.com.au

Industry/Entity Type

Shop

Contact Information for Business Card

Linda Farrugia
Ph 0437 620 915

Logo Text

Farrugia's Quality Meats

Logo styles of interest
Pictorial/Combination Logo
Requirements
Must have
• We use Century Gothic Font

```html
<!DOCTYPE html>
<html lang="en">
<head>
<meta charset="utf-8">
<title>Farrugia's Quality Meats – Business Cards</title>
<link rel="stylesheet" href="https://fonts.googleapis.com/css2?family=Questrial&family=Arimo&display=swap">
<style>
  :root{
    --sheet:#ebeceb;
    --sky:#7ae1fc;
    --ink:#2b2a29;
    --paper:#ffffff;
    --label:#333333;
  }
  *{margin:0;padding:0;box-sizing:border-box}
  html,body{width:1200px;height:839px;overflow:hidden;background:var(--sheet)}
  .sheet{position:relative;width:1200px;height:839px;font-family:"Questrial","Century Gothic",sans-serif;color:var(--ink)}
  .side-label,.row-number{position:absolute;font-family:"Arimo",Arial,sans-serif;color:var(--label);font-size:23px}
  .side-label{transform:translateX(-50%)}
  .card{position:absolute;width:515px;height:287px;box-shadow:2px 6px 10px rgba(0,0,0,.12);overflow:hidden}
  .card--sky{background:var(--sky)}
  .card--paper{background:var(--paper);border:1px solid #c9c9c9}
  .card > *{position:absolute}
  .brand{text-align:center;line-height:1.12;white-space:nowrap;transform:translateX(-50%)}
  .divider{width:6px}
  .line{white-space:nowrap;font-size:13.8px;transform:translateY(-50%)}
  .line--small{font-size:13.4px}
  .line--strong{font-weight:700}
  .icon{width:10px;height:10px;transform:translateY(-50%)}
  .person{text-align:right;white-space:nowrap}
  .person__name{display:block;font-weight:700;font-size:17px}
  .person__role{display:block;font-size:17px;margin-top:6px}
  .contact{font-size:16.5px;white-space:nowrap;transform:translateY(-50%)}
  .bands{left:0;bottom:0;width:100%;height:100%}
</style>
</head>
<body>
<div class="sheet">
  <span class="side-label" style="left:341px;top:57px">Front</span>
  <span class="side-label" style="left:907px;top:60px">Back</span>
  <span class="row-number" style="left:46px;top:106px">1</span>
  <span class="row-number" style="left:46px;top:488px">2</span>

  <!-- Shop card, front -->
  <section class="card card--sky" style="left:81px;top:102px">
    <div class="brand" style="left:97px;top:146px;font-size:19px">Farrugia's<br>Quality Meats</div>
    <svg class="divider" style="left:171px;top:86px;height:125px" viewBox="0 0 6 125" aria-hidden="true"><polygon points="3,0 4.5,62 3,125 1.5,62" fill="var(--ink)"/></svg>
    <span class="line" style="left:202px;top:89px">Shop 9, Ridgeway Court, Bellmoor NSW 2341</span>
    <svg class="icon" style="left:190px;top:109px" viewBox="0 0 24 24" aria-hidden="true"><path d="M6.6 10.8a15 15 0 0 0 6.6 6.6l2.2-2.2c.3-.3.7-.4 1-.2 1.1.4 2.3.6 3.6.6.6 0 1 .4 1 1V20c0 .6-.4 1-1 1A17 17 0 0 1 3 4c0-.6.4-1 1-1h3.5c.6 0 1 .4 1 1 0 1.3.2 2.5.6 3.6.1.3 0 .7-.2 1z" fill="var(--ink)"/></svg>
    <span class="line line--strong" style="left:202px;top:109px">02 6512 3840</span>
    <span class="line" style="left:202px;top:149px">47 Marlow St, Corrindale NSW 2344</span>
    <svg class="icon" style="left:190px;top:169px" viewBox="0 0 24 24" aria-hidden="true"><path d="M6.6 10.8a15 15 0 0 0 6.6 6.6l2.2-2.2c.3-.3.7-.4 1-.2 1.1.4 2.3.6 3.6.6.6 0 1 .4 1 1V20c0 .6-.4 1-1 1A17 17 0 0 1 3 4c0-.6.4-1 1-1h3.5c.6 0 1 .4 1 1 0 1.3.2 2.5.6 3.6.1.3 0 .7-.2 1z" fill="var(--ink)"/></svg>
    <span class="line line--strong" style="left:202px;top:169px">02 6518 2274</span>
    <span class="line" style="left:202px;top:208px">ABN 48 907 215 816</span>
  </section>

  <!-- Shop card, back -->
  <section class="card card--paper" style="left:656px;top:102px">
    <div class="brand" style="left:96px;top:130px;font-size:15.5px">Farrugia's<br>Quality Meats</div>
    <span class="line line--small" style="left:217px;top:77px">Shop 9, Ridgeway Court, Bellmoor NSW 2341</span>
    <svg class="icon" style="left:203px;top:96px" viewBox="0 0 24 24" aria-hidden="true"><path d="M6.6 10.8a15 15 0 0 0 6.6 6.6l2.2-2.2c.3-.3.7-.4 1-.2 1.1.4 2.3.6 3.6.6.6 0 1 .4 1 1V20c0 .6-.4 1-1 1A17 17 0 0 1 3 4c0-.6.4-1 1-1h3.5c.6 0 1 .4 1 1 0 1.3.2 2.5.6 3.6.1.3 0 .7-.2 1z" fill="var(--ink)"/></svg>
    <span class="line line--small" style="left:217px;top:96px">02 6512 3840</span>
    <span class="line line--small" style="left:217px;top:134px">47 Marlow St, Corrindale NSW 2344</span>
    <svg class="icon" style="left:203px;top:152px" viewBox="0 0 24 24" aria-hidden="true"><path d="M6.6 10.8a15 15 0 0 0 6.6 6.6l2.2-2.2c.3-.3.7-.4 1-.2 1.1.4 2.3.6 3.6.6.6 0 1 .4 1 1V20c0 .6-.4 1-1 1A17 17 0 0 1 3 4c0-.6.4-1 1-1h3.5c.6 0 1 .4 1 1 0 1.3.2 2.5.6 3.6.1.3 0 .7-.2 1z" fill="var(--ink)"/></svg>
    <span class="line line--small" style="left:217px;top:152px">02 6518 2274</span>
    <span class="line line--small" style="left:217px;top:191px">ABN 48 907 215 816</span>
    <svg class="bands" viewBox="0 0 534 297" preserveAspectRatio="none" aria-hidden="true">
      <polygon points="0,246 202,246 238,272 534,272 534,291 0,291" fill="var(--sky)"/>
      <polygon points="226,254 531,254 531,269 248,269" fill="var(--ink)"/>
    </svg>
  </section>

  <!-- Personal card, front -->
  <section class="card card--sky" style="left:83px;top:487px">
    <div class="person" style="right:351px;top:125px">
      <span class="person__name">Linda Farrugia</span>
      <span class="person__role">Accounts</span>
    </div>
    <svg class="divider" style="left:170px;top:89px;height:120px" viewBox="0 0 6 120" aria-hidden="true"><polygon points="3,0 4.5,60 3,120 1.5,60" fill="var(--ink)"/></svg>
    <svg class="icon" style="left:197px;top:135px" viewBox="0 0 24 24" aria-hidden="true"><path d="M6.6 10.8a15 15 0 0 0 6.6 6.6l2.2-2.2c.3-.3.7-.4 1-.2 1.1.4 2.3.6 3.6.6.6 0 1 .4 1 1V20c0 .6-.4 1-1 1A17 17 0 0 1 3 4c0-.6.4-1 1-1h3.5c.6 0 1 .4 1 1 0 1.3.2 2.5.6 3.6.1.3 0 .7-.2 1z" fill="var(--ink)"/></svg>
    <span class="contact" style="left:213px;top:135px">0437 620 915</span>
    <svg class="icon" style="left:197px;top:160px" viewBox="0 0 24 24" aria-hidden="true"><path d="M2 5h20v14H2z" fill="var(--ink)"/><path d="M2 5l10 8 10-8" fill="none" stroke="var(--sky)" stroke-width="2"/></svg>
    <span class="contact" style="left:213px;top:160px">lindafarrugia@quollmail.com.au</span>
  </section>

  <!-- Personal card, back -->
  <section class="card card--paper" style="left:665px;top:486px">
    <div class="person" style="right:333px;top:118px">
      <span class="person__name">Linda Farrugia</span>
      <span class="person__role">Accounts</span>
    </div>
    <svg class="icon" style="left:208px;top:127px" viewBox="0 0 24 24" aria-hidden="true"><path d="M6.6 10.8a15 15 0 0 0 6.6 6.6l2.2-2.2c.3-.3.7-.4 1-.2 1.1.4 2.3.6 3.6.6.6 0 1 .4 1 1V20c0 .6-.4 1-1 1A17 17 0 0 1 3 4c0-.6.4-1 1-1h3.5c.6 0 1 .4 1 1 0 1.3.2 2.5.6 3.6.1.3 0 .7-.2 1z" fill="var(--ink)"/></svg>
    <span class="contact" style="left:231px;top:127px;font-size:16px">0437 620 915</span>
    <svg class="icon" style="left:208px;top:153px" viewBox="0 0 24 24" aria-hidden="true"><path d="M2 5h20v14H2z" fill="var(--ink)"/><path d="M2 5l10 8 10-8" fill="none" stroke="var(--paper)" stroke-width="2"/></svg>
    <span class="contact" style="left:231px;top:153px;font-size:16px">lindafarrugia@quollmail.com.au</span>
    <svg class="bands" viewBox="0 0 534 297" preserveAspectRatio="none" aria-hidden="true">
      <polygon points="0,246 202,246 238,272 534,272 534,291 0,291" fill="var(--sky)"/>
      <polygon points="226,254 531,254 531,269 248,269" fill="var(--ink)"/>
    </svg>
  </section>
</div>
</body>
</html>
```